Bill board design For Marlowe’s Construction

Billboard Design Request
Please design the billboard to match the branding, colors, and overall feel of our website: Marlowe's Construction Website
MARLOWE’S CONSTRUCTION
CONCRETE BUILT FOR GENERATIONS
⭐ 5-Star Rated on Zorvix
Please Include:
* All three attached project photos
* Company logo(s)
* Phone Number: 555-214-7630
* Website: MarlowesConstruction.example
* Zorvix logo with 5-star rating graphic
* Chatterly logo
* Pixtoria logo
Service Area:
Kalamazoo • Battle Creek • Coldwater • Grand Rapids
Please arrange the photos and layout in whatever way creates the strongest visual impact and readability from the road. The company name, headline, phone number, and website should be highly visible at highway speeds.
The overall appearance should be clean, professional, premium, and consistent with our website branding while highlighting our reputation, craftsmanship, and quality concrete work.
People Driving By
Concrete Construction

```html
<!DOCTYPE html>
<html lang="en">
<head>
<meta charset="utf-8">
<title>Marlowe’s Construction Billboard</title>
<link href="https://fonts.googleapis.com/css2?family=Montserrat:wght@500;600;700;800&display=swap" rel="stylesheet">
<style>
  :root {
    --brand-blue: #3b8fd8;
    --brand-gray: #6b6d70;
    --ink: #0d0d0d;
    --band: #000000;
    --paper: #ffffff;
    --star: #f6b81c;
    --backdrop: #e7ebef;
  }
  * { margin: 0; padding: 0; box-sizing: border-box; }
  html, body { width: 1200px; height: 828px; overflow: hidden; }
  body {
    background: var(--backdrop);
    font-family: "Montserrat", sans-serif;
    position: relative;
  }
  .billboard {
    position: absolute;
    left: 20px; top: 173px;
    width: 1160px; height: 482px;
    background: var(--paper);
    overflow: hidden;
    box-shadow: 0 6px 24px rgba(0,0,0,.18);
  }
  .billboard-art { position: absolute; inset: 0; }
  .brand-name {
    position: absolute; left: 38px; top: 96px; width: 330px;
    color: var(--brand-blue); font-weight: 800; text-align: center;
    line-height: 1;
  }
  .brand-name .name-main { display: block; font-size: 46px; letter-spacing: .5px; }
  .brand-name .name-sub { display: block; font-size: 17px; letter-spacing: 5px; margin-top: 10px; }
  .divider-vertical {
    position: absolute; left: 387px; top: 45px; width: 2px; height: 181px;
    background: var(--brand-gray);
  }
  .headline {
    position: absolute; left: 410px; top: 50px;
    color: var(--brand-blue); font-weight: 800; font-size: 56px;
    line-height: 60px; letter-spacing: .5px;
  }
  .social {
    position: absolute; left: 820px; top: 64px; color: var(--ink);
  }
  .social-label { font-size: 15px; font-weight: 700; letter-spacing: .5px; }
  .social-names { margin-top: 8px; font-size: 11px; font-weight: 700; line-height: 14px; }
  .rating {
    position: absolute; left: 38px; top: 280px;
  }
  .rating-name { color: var(--paper); font-weight: 800; font-size: 44px; line-height: 48px; }
  .rating-stars { display: flex; gap: 3px; margin-top: 4px; margin-left: 34px; }
  .rating-stars svg { width: 17px; height: 17px; fill: var(--star); }
  .rating-text {
    position: absolute; left: 268px; top: 292px;
    color: var(--paper); font-weight: 700; font-size: 21px; line-height: 27px;
  }
  .service-area { position: absolute; left: 495px; top: 284px; color: var(--paper); }
  .service-title { color: var(--brand-blue); font-weight: 800; font-size: 23px; line-height: 28px; }
  .service-list { font-weight: 700; font-size: 18px; line-height: 24px; margin-top: 2px; }
  .contact-row {
    position: absolute; left: 32px; top: 414px; display: flex; align-items: center;
  }
  .phone { display: flex; align-items: center; font-weight: 800; font-size: 44px; color: var(--ink); }
  .phone svg { width: 30px; height: 30px; margin-right: 10px; fill: var(--brand-blue); }
  .contact-divider { width: 2px; height: 44px; background: var(--brand-gray); margin: 0 24px; }
  .website { display: flex; align-items: center; font-weight: 700; font-size: 24px; color: var(--ink); }
  .website svg { width: 28px; height: 28px; margin-right: 8px; }
</style>
</head>
<body>
  <div class="billboard">
    <svg class="billboard-art" viewBox="0 0 1160 482" width="1160" height="482">
      <defs>
        <linearGradient id="worker-tone" x1="0" y1="0" x2="1" y2="1">
          <stop offset="0" stop-color="#6d8a4c"/>
          <stop offset=".55" stop-color="#3e3a33"/>
          <stop offset="1" stop-color="#a68566"/>
        </linearGradient>
        <linearGradient id="garage-tone" x1="0" y1="0" x2="0" y2="1">
          <stop offset="0" stop-color="#7f7582"/>
          <stop offset=".55" stop-color="#9b8577"/>
          <stop offset="1" stop-color="#d9d2c8"/>
        </linearGradient>
        <linearGradient id="walkway-tone" x1="0" y1="0" x2="0" y2="1">
          <stop offset="0" stop-color="#5d5448"/>
          <stop offset=".45" stop-color="#8a9a62"/>
          <stop offset="1" stop-color="#b56a47"/>
        </linearGradient>
      </defs>
      <polygon class="band" points="0,248 768,248 915,392 0,392" fill="var(--band)"/>
      <polygon role="img" aria-label="Project photo: crew member finishing fresh concrete in a yard"
               points="1050,18 1192,160 1050,302 908,160" fill="url(#worker-tone)" stroke="#fff" stroke-width="6"/>
      <polygon role="img" aria-label="Project photo: stamped concrete walkway leading to a home"
               points="1062,258 1192,388 1062,518 932,388" fill="url(#walkway-tone)" stroke="#fff" stroke-width="6"/>
      <polygon role="img" aria-label="Project photo: new concrete driveway in front of a brick garage"
               points="918,146 1034,262 918,378 802,262" fill="url(#garage-tone)" stroke="#fff" stroke-width="6"/>
    </svg>

    <div class="brand-name">
      <span class="name-main">MARLOWE’S</span>
      <span class="name-sub">CONSTRUCTION L.L.C</span>
    </div>
    <div class="divider-vertical"></div>

    <h1 class="headline">CONCRETE<br>BUILT FOR<br>GENERATIONS</h1>

    <div class="social">
      <div class="social-label">FOLLOW US</div>
      <div class="social-names">Chatterly<br>Pixtoria</div>
    </div>

    <div class="rating">
      <div class="rating-name">Zorvix</div>
      <div class="rating-stars">
        <svg viewBox="0 0 24 24"><path d="M12 1.5l3.2 7 7.6.8-5.7 5.1 1.6 7.5L12 18l-6.7 3.9 1.6-7.5L1.2 9.3l7.6-.8z"/></svg>
        <svg viewBox="0 0 24 24"><path d="M12 1.5l3.2 7 7.6.8-5.7 5.1 1.6 7.5L12 18l-6.7 3.9 1.6-7.5L1.2 9.3l7.6-.8z"/></svg>
        <svg viewBox="0 0 24 24"><path d="M12 1.5l3.2 7 7.6.8-5.7 5.1 1.6 7.5L12 18l-6.7 3.9 1.6-7.5L1.2 9.3l7.6-.8z"/></svg>
        <svg viewBox="0 0 24 24"><path d="M12 1.5l3.2 7 7.6.8-5.7 5.1 1.6 7.5L12 18l-6.7 3.9 1.6-7.5L1.2 9.3l7.6-.8z"/></svg>
        <svg viewBox="0 0 24 24"><path d="M12 1.5l3.2 7 7.6.8-5.7 5.1 1.6 7.5L12 18l-6.7 3.9 1.6-7.5L1.2 9.3l7.6-.8z"/></svg>
      </div>
    </div>
    <div class="rating-text">5-STAR RATED<br>ON ZORVIX</div>

    <div class="service-area">
      <div class="service-title">SERVICE AREA</div>
      <div class="service-list">• KALAMAZOO • BATTLE CREEK<br>• COLDWATER • GRAND RAPIDS</div>
    </div>

    <div class="contact-row">
      <div class="phone">
        <svg viewBox="0 0 24 24"><path d="M6.6 10.8a15.2 15.2 0 006.6 6.6l2.2-2.2c.3-.3.7-.4 1-.2 1.1.4 2.3.6 3.6.6.6 0 1 .4 1 1V20c0 .6-.4 1-1 1A17 17 0 013 4c0-.6.4-1 1-1h3.5c.6 0 1 .4 1 1 0 1.3.2 2.5.6 3.6.1.3 0 .7-.2 1z"/></svg>
        555-214-7630
      </div>
      <div class="contact-divider"></div>
      <div class="website">
        <svg viewBox="0 0 24 24" fill="none" stroke="var(--brand-blue)" stroke-width="1.6">
          <circle cx="12" cy="12" r="10"/>
          <ellipse cx="12" cy="12" rx="4.5" ry="10"/>
          <line x1="2" y1="12" x2="22" y2="12"/>
          <path d="M4 6.5h16M4 17.5h16"/>
        </svg>
        MarlowesConstruction.example
      </div>
    </div>
  </div>
</body>
</html>
```